BKT Consulting

Government/Entitlement Consulting Services- I assist developers obtain entitlements from local, state and federal government agencies so that they can build their projects. Often these projects are very complicated and political and may face community opposition.

Target Market(s)

Real Estate Developers

Industry/Entity Type

Business Consultant

Contact Information for Business Card

Dana Velmonte
Principal

Font styles to use
Serif
Sans Serif

Requirements
Must have
• Classy and professional appeal.
Nice to have
• I like a combination of a mat and glossy finish. I've seen that done with black and then a bold color for a pop, but am not 100% committed to that.

```html
<!DOCTYPE html>
<html lang="en">
<head>
<meta charset="UTF-8">
<title>BKT Consulting – Business Card</title>
<link rel="stylesheet" href="https://fonts.googleapis.com/css2?family=Michroma&display=swap">
<style>
  :root {
    --backdrop: #cfcfcf;
    --card: #1d1c1c;
    --mark: #e9e9e9;
    --name: #a9a9a9;
    --title: #8a8a8a;
  }
  * { margin: 0; padding: 0; box-sizing: border-box; }
  html, body {
    width: 1200px;
    height: 960px;
    overflow: hidden;
    background: var(--backdrop);
  }
  .canvas {
    width: 1200px;
    height: 960px;
    display: flex;
    flex-direction: column;
    align-items: center;
    justify-content: center;
    gap: 56px;
  }
  .card {
    position: relative;
    width: 700px;
    height: 400px;
    background: var(--card);
    font-family: "Michroma", sans-serif;
  }
  .brand {
    display: flex;
    align-items: center;
    gap: 16px;
    color: var(--mark);
    text-transform: uppercase;
    letter-spacing: 0.08em;
    white-space: nowrap;
  }
  .brand-square {
    background: var(--mark);
    flex: none;
  }
  .card-front .brand {
    position: absolute;
    left: 50%;
    top: 50%;
    transform: translate(-50%, -50%);
    font-size: 34px;
  }
  .card-front .brand-square { width: 26px; height: 26px; }
  .card-back .brand {
    position: absolute;
    right: 52px;
    top: 98px;
    font-size: 20px;
    gap: 10px;
  }
  .card-back .brand-square { width: 15px; height: 15px; }
  .contact {
    position: absolute;
    left: 84px;
    top: 234px;
    text-transform: uppercase;
  }
  .contact-name {
    color: var(--name);
    font-size: 19px;
    letter-spacing: 0.06em;
  }
  .contact-title {
    margin-top: 12px;
    color: var(--title);
    font-size: 12px;
    letter-spacing: 0.06em;
  }
</style>
</head>
<body>
  <main class="canvas">
    <section class="card card-front">
      <div class="brand">
        <span class="brand-square"></span>
        <span class="brand-name">BKT Consulting</span>
      </div>
    </section>
    <section class="card card-back">
      <div class="brand">
        <span class="brand-square"></span>
        <span class="brand-name">BKT Consulting</span>
      </div>
      <div class="contact">
        <p class="contact-name">Dana Velmonte</p>
        <p class="contact-title">Principal</p>
      </div>
    </section>
  </main>
</body>
</html>
```